Brindle Motor Finance- Free Oil Change letters

this is A Letter from my Used Car Sales & Service business. Specifically this is in a large window envelope (See Web Links) A free oil change to get this specific customer to open the envelope. The free oil change is the top have of the letter stuff in 4 1/8 x 9 open window envelope. The rest of letter is to the Fresh bankruptcy people. The coupon is to get them to open and read my offer. I had the combined ideas from the moving target link attached.
the middle of the envelope has to have a customer name address for postal delivery
I have also included our company website and our logo to be contained. This has to be in a letter program that I will mail merge a database mailer to print.

This project is for only what will be view through the large window envelope

my company website
http://www.gobmf-example.com/

envelope I use
http://www.mailpouchdepot-example.com/envelopes/window/full-view-window/envelope-71936.html

Envelope Dimensions: 4 1/8 x 9 1/2
Window Dimensions: 3 x 8 (From Left Edge: 3/4 - From Bottom Edge: 1/2)

the whole point is the make this look highend to get the customer to want read the letter.. The Letter will talk about We are the Fresh Lane Lending Pro and to come to us to buy a used car.

```html
<!DOCTYPE html>
<html lang="en">
<head>
<meta charset="utf-8">
<title>Brindle Motor Finance – Free Oil Change</title>
<link rel="stylesheet" href="https://fonts.googleapis.com/css2?family=League+Gothic&family=Archivo+Narrow:wght@400&display=swap">
<style>
  :root {
    --maroon-deep: #2e0806;
    --maroon: #5a0f0a;
    --red: #a8180c;
    --orange: #e0661a;
    --amber: #f4b52a;
    --glow: #fff4c8;
    --gold-line: #c9a24a;
    --ink: #0c0a08;
    --brand: #f5c21a;
  }
  * { margin: 0; padding: 0; box-sizing: border-box; }
  html, body {
    width: 1200px;
    height: 450px;
    overflow: hidden;
    background: var(--maroon-deep);
  }
  .banner {
    position: relative;
    width: 1200px;
    height: 450px;
    overflow: hidden;
  }
  .banner__glow {
    position: absolute;
    inset: 0;
    background:
      radial-gradient(ellipse 330px 230px at 600px 190px, var(--glow) 0%, rgba(255,228,140,0.85) 35%, rgba(244,181,42,0) 100%),
      radial-gradient(ellipse 520px 330px at 600px 210px, var(--amber) 0%, var(--orange) 45%, rgba(168,24,12,0.6) 75%, rgba(90,15,10,0) 100%),
      radial-gradient(circle 170px at 1110px 230px, rgba(244,181,42,0.55) 0%, rgba(244,181,42,0) 100%),
      radial-gradient(circle 150px at 110px 330px, rgba(244,181,42,0.45) 0%, rgba(244,181,42,0) 100%),
      radial-gradient(ellipse 700px 420px at 600px 180px, var(--red) 0%, var(--maroon) 65%, var(--maroon-deep) 100%);
  }
  .banner__frame {
    position: absolute;
    inset: 0;
  }
  .offer {
    position: absolute;
    left: 0;
    right: 0;
    top: 152px;
    text-align: center;
    color: var(--ink);
  }
  .offer__headline {
    font-family: "League Gothic", "Arial Narrow", sans-serif;
    font-weight: 400;
    font-size: 136px;
    line-height: 1;
    letter-spacing: 1px;
    margin-left: -30px;
  }
  .offer__details {
    font-family: "Archivo Narrow", "Arial Narrow", sans-serif;
    font-size: 18px;
    letter-spacing: 1.1px;
    word-spacing: 3px;
    margin-top: -4px;
    margin-left: -30px;
    white-space: pre;
  }
  .brand {
    position: absolute;
    right: 36px;
    bottom: 38px;
    display: flex;
    align-items: center;
    gap: 6px;
  }
  .brand__mark {
    width: 10px;
    height: 10px;
    background: var(--brand);
  }
  .brand__name {
    font-family: "League Gothic", "Arial Narrow", sans-serif;
    font-size: 22px;
    line-height: 1;
    color: var(--brand);
    letter-spacing: 0.5px;
  }
</style>
</head>
<body>
  <main class="banner">
    <div class="banner__glow" role="img" aria-label="Glowing gold and amber bokeh lights with firework sparks over a deep red background"></div>

    <svg class="banner__frame" width="1200" height="450" viewBox="0 0 1200 450" aria-hidden="true">
      <rect x="12" y="22" width="1176" height="411" fill="none" stroke="var(--gold-line)" stroke-width="1.5"/>
      <rect x="20" y="30" width="1160" height="395" fill="none" stroke="var(--gold-line)" stroke-width="1.5"/>
    </svg>

    <section class="offer">
      <h1 class="offer__headline">FREE OIL!</h1>
      <p class="offer__details">Free Lube,  Oil &amp; Filter Change .. a $25,95 Vale!</p>
    </section>

    <div class="brand">
      <span class="brand__mark"></span>
      <span class="brand__name">Brindle Motor Finance</span>
    </div>
  </main>
</body>
</html>
```